New Web Design Project

website name will be called www.brightmarasun.com
Please us color red, white,grey if possible
We are a solar provider that will offer solar ownership and leases with 25yr warranty and labor. Over 20yrs combined solar experience

Number of Pages Required

1 page

```html
<!DOCTYPE html>
<html lang="en">
<head>
<meta charset="utf-8">
<title>Brightmara Sun — Solar Energy Provider</title>
<link href="https://fonts.googleapis.com/css2?family=Orbitron:wght@700;800;900&family=Poppins:wght@400;500;600;700&display=swap" rel="stylesheet">
<style>
:root{
  --red:#c50d0d;
  --red-deep:#a10a0a;
  --ink:#1d1d1d;
  --text:#555;
  --grey:#efefef;
  --grey-mid:#9d9d9d;
  --grey-dark:#8a8a8a;
  --white:#fff;
}
*{margin:0;padding:0;box-sizing:border-box}
html,body{width:1200px;height:3779px;overflow:hidden}
body{position:relative;background:var(--white);font-family:"Poppins",sans-serif;color:var(--text)}
.abs{position:absolute}
.display{font-family:"Orbitron",sans-serif;font-weight:800;color:var(--ink);text-transform:uppercase;letter-spacing:1px}
.eyebrow{font-family:"Poppins",sans-serif;font-weight:600;color:var(--red);font-size:15px;letter-spacing:.5px;text-transform:uppercase}
.btn{display:flex;align-items:center;justify-content:center;background:var(--red);color:var(--white);font-weight:600;font-size:13px;text-transform:uppercase;letter-spacing:.3px}
.center{left:0;width:1200px;text-align:center}

.bg-shapes{left:0;top:0;width:1200px;height:3779px}

/* header */
.topbar{left:733px;top:0;width:467px;height:32px;background:var(--red);clip-path:polygon(18px 0,100% 0,100% 100%,0 100%);display:flex;align-items:center;justify-content:flex-end;gap:26px;padding-right:90px;color:var(--white);font-size:14px;font-weight:500}
.topbar span{display:flex;align-items:center;gap:6px}
.brand{display:flex;align-items:center;gap:10px;font-family:"Poppins",sans-serif;font-weight:600;color:var(--grey-dark);white-space:nowrap}
.brand-dot{width:14px;height:14px;border-radius:50%;background:var(--red);flex:none}
.nav{top:50px;left:606px;font-size:14px;font-weight:600;color:var(--ink)}
.nav a{position:absolute;white-space:nowrap;color:var(--ink);text-decoration:none}
.nav a.active{color:var(--red)}

/* hero */
.hero-photo{left:0;top:88px;width:1200px;height:682px;background:linear-gradient(120deg,#4a5a6e 0%,#6e7f93 35%,#93a6bb 60%,#c9d3dc 100%)}
.hero-title{left:84px;top:318px;font-size:44px;line-height:44px;color:var(--white);font-weight:800;letter-spacing:2px}
.hero-sub{left:86px;top:413px;width:520px;font-size:20px;line-height:25px;color:var(--white);font-weight:500}
.hero-btn{left:87px;top:481px;width:117px;height:30px}

/* about */
.about-photo{left:85px;top:905px;width:435px;height:435px;border-radius:50%;background:linear-gradient(160deg,#3f7fd6,#2a5aa8 55%,#1e3d74)}
.about-eyebrow{left:595px;top:932px}
.about-title{left:594px;top:955px;font-size:31px;line-height:35px}
.about-title em{font-style:normal;color:var(--red)}
.about-lead{left:594px;top:1028px;width:470px;font-size:14px;line-height:22px}
.feature{left:592px;display:flex;gap:16px}
.feature h4{font-size:17px;font-weight:500;color:var(--ink);margin-bottom:6px}
.feature p{font-size:13.5px;line-height:21px;width:300px}
.about-btn{left:594px;top:1279px;width:119px;height:30px}

/* services */
.services-eyebrow{top:1513px}
.services-title{top:1533px;font-size:32px}
.service-card{top:1599px;width:281px;height:236px;background:var(--white);box-shadow:0 4px 18px rgba(0,0,0,.06);text-align:center;padding-top:36px}
.service-card svg{display:block;margin:0 auto;height:72px}
.service-card h3{font-size:19px;font-weight:500;color:var(--ink);margin-top:10px}
.service-card p{font-size:13.5px;line-height:18px;margin-top:6px}

/* projects */
.projects-eyebrow{top:2026px}
.projects-title{top:2046px;font-size:32px;line-height:35px}
.project{top:2145px;width:240px;height:314px}
.project-tag{left:720px;top:2400px;width:241px;height:95px;background:var(--red);padding:26px 0 0 19px;color:var(--white);font-family:"Orbitron",sans-serif;font-weight:800;font-size:19px;line-height:20px;text-transform:uppercase;display:flex;gap:14px;align-items:flex-end}

/* testimonials */
.testi-eyebrow{top:2592px}
.testi-title{top:2612px;font-size:32px;line-height:35px}
.testi-card{top:2708px;width:329px;height:236px;background:#f6f6f6;padding:26px 22px 0 38px}
.testi-head{display:flex;align-items:center;gap:18px}
.avatar{width:62px;height:62px;border-radius:50%}
.testi-name{font-size:14px;font-weight:600;color:var(--ink)}
.testi-role{font-size:13px;color:var(--red);margin-top:2px}
.testi-text{font-size:13.5px;line-height:20px;margin-top:16px}
.stars{display:flex;gap:13px;margin-top:12px}
.quote{position:absolute;right:40px;bottom:26px}
.dots{top:2970px;left:585px;display:flex;gap:5px}
.dots i{width:7px;height:7px;border-radius:50%;background:#cfcfcf}
.dots i.on{background:var(--red)}

/* newsletter */
.news-eyebrow{top:3125px;color:var(--white)}
.news-title{top:3148px;font-size:31px;line-height:33px;color:var(--white)}
.news-input{left:279px;top:3227px;width:472px;height:41px;background:var(--white);font-size:16px;color:#666;padding:10px 22px}
.news-btn{left:751px;top:3227px;width:170px;height:41px;background:var(--grey-mid);font-size:16px}

/* footer */
.foot-brand{left:120px;top:3590px;font-size:26px}
.foot-head{font-family:"Poppins",sans-serif;font-weight:600;font-size:19px;color:var(--ink);top:3490px;letter-spacing:.5px}
.foot-links{left:434px;top:3524px;font-size:12.5px;line-height:23.3px;color:var(--text)}
.news-item{left:622px;display:flex;gap:14px}
.news-thumb{width:52px;height:50px;background:linear-gradient(135deg,#3c6fb7,#7aa0d0);flex:none}
.news-item h5{font-size:13.5px;line-height:18px;font-weight:600;color:var(--ink);width:180px}
.news-item small{font-size:10.5px;font-weight:600;color:var(--ink)}
.contact-list{left:907px;top:3528px;font-size:12.5px;line-height:17px;color:var(--text)}
.contact-list div{display:flex;gap:6px;margin-bottom:5px}
.socials{left:907px;top:3620px;display:flex;gap:6px}
.socials i{width:24px;height:24px;border-radius:50%}
.copybar{left:0;top:3733px;width:1200px;height:46px;background:#a3a3a3;color:var(--white);font-size:14px;font-weight:500;display:flex;align-items:center;justify-content:center}
.to-top{left:1129px;top:3718px;width:31px;height:31px;border-radius:50%;background:var(--red);display:flex;align-items:center;justify-content:center}
</style>
</head>
<body>

<svg class="abs bg-shapes" viewBox="0 0 1200 3779" aria-hidden="true">
  <path d="M0 1700 Q 300 1380 720 1379 Q 1000 1380 1200 1420 L1200 1932 L0 1932Z" fill="#efefef"/>
  <path d="M820 745 Q 1110 820 1200 1040" fill="none" stroke="#c50d0d" stroke-width="4"/>
  <path d="M0 3030 Q 600 2990 1200 3040 L1200 3380 L0 3660Z" fill="#b20d0d"/>
  <path d="M0 3030 Q 600 2990 1200 3040 L1200 3100 Q 700 3060 0 3120Z" fill="#c81414" opacity=".6"/>
  <path d="M0 3665 Q 260 3340 1200 3375 L1200 3733 L0 3733Z" fill="#fff"/>
</svg>

<!-- header -->
<div class="abs topbar">
  <span><svg width="12" height="12" viewBox="0 0 24 24"><path d="M6.6 10.8a15 15 0 0 0 6.6 6.6l2.2-2.2c.3-.3.7-.4 1-.2 1.1.4 2.3.6 3.6.6.6 0 1 .4 1 1V20c0 .6-.4 1-1 1A17 17 0 0 1 3 4c0-.6.4-1 1-1h3.5c.6 0 1 .4 1 1 0 1.2.2 2.4.6 3.6.1.3 0 .7-.2 1z" fill="#fff"/></svg>+012 (555) 0148</span>
  <span><svg width="13" height="10" viewBox="0 0 26 20"><rect width="26" height="20" rx="2" fill="#fff"/><path d="M1 2l12 9 12-9" fill="none" stroke="#c50d0d" stroke-width="2"/></svg>hello@brightmarasun.com</span>
</div>
<div class="abs brand" style="left:88px;top:32px;font-size:24px"><span class="brand-dot"></span>Brightmara Sun</div>
<nav class="abs nav">
  <a class="active" href="#" style="left:0">HOME</a>
  <a href="#" style="left:73px">ABOUT US</a>
  <a href="#" style="left:177px">SERVICE</a>
  <a href="#" style="left:268px">PROJECT</a>
  <a href="#" style="left:364px">SHOP</a>
  <a href="#" style="left:434px">CONTACT</a>
</nav>

<!-- hero -->
<div class="abs hero-photo" role="img" aria-label="Two engineers in hard hats inspecting rooftop solar panels"></div>
<h1 class="abs display hero-title">Solar Energy<br>Provider Agency</h1>
<p class="abs hero-sub">Solar ownership and leases backed by a 25-year warranty and labor.</p>
<a class="abs btn hero-btn">Get Started</a>
<svg class="abs" style="left:589px;top:609px" width="20" height="32" viewBox="0 0 20 32" aria-hidden="true"><rect x="1" y="1" width="18" height="30" rx="9" fill="none" stroke="#fff" stroke-width="2"/><line x1="10" y1="8" x2="10" y2="14" stroke="#fff" stroke-width="2"/></svg>
<svg class="abs" style="left:0;top:690px" width="1200" height="100" viewBox="0 0 1200 100" aria-hidden="true">
  <path d="M0 40 Q 450 -15 1200 45 L1200 100 L0 100Z" fill="#c50d0d"/>
  <path d="M0 80 Q 520 -2 1200 52 L1200 100 L0 100Z" fill="#fff"/>
</svg>

<!-- about -->
<svg class="abs" style="left:70px;top:868px" width="490" height="490" viewBox="0 0 490 490" aria-hidden="true">
  <path d="M38 150 A 225 225 0 0 1 470 220" fill="none" stroke="#c50d0d" stroke-width="9" stroke-linecap="round"/>
</svg>
<div class="abs about-photo" role="img" aria-label="Technician in an orange hard hat installing solar panels with a drill"></div>
<div class="abs eyebrow about-eyebrow">Why Choose Us</div>
<h2 class="abs display about-title">We Have <em>20</em><br>Years of Experience</h2>
<p class="abs about-lead">Over 20 years of combined solar experience, from first design to final panel, for homes and businesses.</p>
<div class="abs feature" style="top:1096px">
  <svg width="32" height="36" viewBox="0 0 32 36" aria-hidden="true"><g fill="none" stroke="#c50d0d" stroke-width="1.6"><path d="M4 4h24l-3 12H7z"/><path d="M10 4v12M16 4v12M22 4v12M5 10h22"/><path d="M16 16v18M10 34h12"/></g></svg>
  <div><h4>Highly-Detailed Solar Solutions</h4><p>Each system is planned for your roof, your usage and your budget.</p></div>
</div>
<div class="abs feature" style="top:1188px">
  <svg width="32" height="36" viewBox="0 0 32 36" aria-hidden="true"><g fill="none" stroke="#c50d0d" stroke-width="1.6"><path d="M4 4h24l-3 12H7z"/><path d="M10 4v12M16 4v12M22 4v12M5 10h22"/><path d="M16 16v18M10 34h12"/></g></svg>
  <div><h4>Best Partner For Renewable Energy</h4><p>Own or lease your panels with labor covered for 25 years.</p></div>
</div>
<a class="abs btn about-btn">Read More</a>

<!-- services -->
<div class="abs center eyebrow services-eyebrow">What We Offer</div>
<h2 class="abs center display services-title">Our Popular Services</h2>
<div class="abs service-card" style="left:167px">
  <svg width="70" height="72" viewBox="0 0 70 72" aria-hidden="true"><g fill="none" stroke="#c50d0d" stroke-width="2"><path d="M8 30 L35 10 L62 30"/><rect x="12" y="30" width="46" height="36"/><rect x="30" y="46" width="10" height="20"/><path d="M16 16h22v8H16zM20 16v8M26 16v8M32 16v8"/><circle cx="56" cy="14" r="7"/></g></svg>
  <h3>Renewable Energy</h3><p>Clean power for your home<br>from day one onward.</p>
</div>
<div class="abs service-card" style="left:459px">
  <svg width="72" height="72" viewBox="0 0 72 72" aria-hidden="true"><g fill="none" stroke="#c50d0d" stroke-width="2"><circle cx="36" cy="36" r="22"/><circle cx="36" cy="36" r="14"/><path d="M36 6v8M36 58v8M6 36h8M58 36h8M15 15l6 6M51 51l6 6M57 15l-6 6M21 51l-6 6"/><path d="M36 44c0-8 4-12 8-12-1 6-4 9-8 12zM36 44c0-8-4-12-8-12 1 6 4 9 8 12z"/></g></svg>
  <h3>Solar Maintenance</h3><p>Regular checks keep every<br>panel at peak output.</p>
</div>
<div class="abs service-card" style="left:750px">
  <svg width="70" height="72" viewBox="0 0 70 76" aria-hidden="true"><g fill="none" stroke="#c50d0d" stroke-width="2"><circle cx="35" cy="26" r="4"/><path d="M35 22 L33 4 L38 4 Z M38 28 L55 36 L53 40 Z M32 28 L16 38 L14 34 Z"/><path d="M33 30 L30 72 H40 L37 30"/><path d="M22 72h26"/><circle cx="35" cy="28" r="22" stroke-dasharray="4 4"/></g></svg>
  <h3>Easy Installation</h3><p>Fast, tidy installs by our<br>own certified crews.</p>
</div>

<!-- projects -->
<div class="abs center eyebrow projects-eyebrow">Projects</div>
<h2 class="abs center display projects-title">We Have Done Many<br>Others Projects</h2>
<div class="abs project" style="left:0;background:linear-gradient(160deg,#7ac043,#3c4a5a)" role="img" aria-label="Worker kneeling on a solar panel"></div>
<div class="abs project" style="left:240px;background:linear-gradient(160deg,#9fb9d6,#3d6aa8 50%,#4c7a3a)" role="img" aria-label="Solar panels on a house roof among trees"></div>
<div class="abs project" style="left:480px;background:linear-gradient(160deg,#dfe6ee,#8b9bb0 50%,#f08b1d)" role="img" aria-label="Engineer with clipboard between solar panel rows"></div>
<div class="abs project" style="left:720px;background:linear-gradient(180deg,#f4c8b4,#e9d6a6 45%,#7d8fa6)" role="img" aria-label="Wind turbines at sunset behind a solar field"></div>
<div class="abs project" style="left:960px;background:linear-gradient(160deg,#c8d8e4,#f0a020 45%,#5d8a3a)" role="img" aria-label="Engineer in hi-vis vest checking solar panels"></div>
<div class="abs project-tag"><span>Solar<br>Engineering</span><svg width="18" height="14" viewBox="0 0 18 14" aria-hidden="true" style="margin-bottom:22px"><path d="M1 7h15M10 1l6 6-6 6" fill="none" stroke="#fff" stroke-width="1.8"/></svg></div>

<!-- testimonials -->
<div class="abs center eyebrow testi-eyebrow">Our Testimonials</div>
<h2 class="abs center display testi-title">What Our Clients Say<br>About Brightmara Sun</h2>

<div class="abs testi-card" style="left:89px">
  <div class="testi-head"><div class="avatar" style="background:#e0a86a" role="img" aria-label="Client portrait"></div><div><div class="testi-name">Marcus T. Reyes</div><div class="testi-role">Software Developer</div></div></div>
  <p class="testi-text">The team explained every option and our lease pays for itself. Install was quick and clean, no mess left at all.</p>
  <div class="stars"><svg width="100" height="16" viewBox="0 0 100 16"><g fill="#a30c0c"><path id="st" d="M8 0l2.4 5 5.6.6-4.2 3.8 1.2 5.6L8 12.2 3 15l1.2-5.6L0 5.6 5.6 5z"/><use href="#st" x="21"/><use href="#st" x="42"/><use href="#st" x="63"/><use href="#st" x="84"/></g></svg></div>
  <svg class="quote" width="54" height="46" viewBox="0 0 54 46" aria-hidden="true"><g fill="none" stroke="#c50d0d" stroke-width="3"><path d="M22 4C10 6 3 14 3 28v14h19V24H10"/><path d="M51 4C39 6 32 14 32 28v14h19V24H39"/></g></svg>
</div>
<div class="abs testi-card" style="left:436px">
  <div class="testi-head"><div class="avatar" style="background:#b88a6e" role="img" aria-label="Client portrait"></div><div><div class="testi-name">Owen R. Fields</div><div class="testi-role">Managing Director</div></div></div>
  <p class="testi-text">Our office bills dropped in the first month. The 25-year warranty gave us real peace of mind going in.</p>
  <div class="stars"><svg width="100" height="16" viewBox="0 0 100 16"><g fill="#a30c0c"><use href="#st"/><use href="#st" x="21"/><use href="#st" x="42"/><use href="#st" x="63"/><use href="#st" x="84"/></g></svg></div>
  <svg class="quote" width="54" height="46" viewBox="0 0 54 46" aria-hidden="true"><g fill="none" stroke="#dcdcdc" stroke-width="3"><path d="M22 4C10 6 3 14 3 28v14h19V24H10"/><path d="M51 4C39 6 32 14 32 28v14h19V24H39"/></g></svg>
</div>
<div class="abs testi-card" style="left:783px">
  <div class="testi-head"><div class="avatar" style="background:#7e8b6a" role="img" aria-label="Client portrait"></div><div><div class="testi-name">Lena Hartwell</div><div class="testi-role">Web Designer</div></div></div>
  <p class="testi-text">Friendly crew, honest pricing and great follow up. I would gladly recommend them to any neighbour.</p>
  <div class="stars"><svg width="100" height="16" viewBox="0 0 100 16"><g fill="#a30c0c"><use href="#st"/><use href="#st" x="21"/><use href="#st" x="42"/><use href="#st" x="63"/><use href="#st" x="84"/></g></svg></div>
  <svg class="quote" width="54" height="46" viewBox="0 0 54 46" aria-hidden="true"><g fill="none" stroke="#dcdcdc" stroke-width="3"><path d="M22 4C10 6 3 14 3 28v14h19V24H10"/><path d="M51 4C39 6 32 14 32 28v14h19V24H39"/></g></svg>
</div>
<div class="abs dots"><i class="on"></i><i></i><i></i></div>

<!-- newsletter -->
<div class="abs center eyebrow news-eyebrow">Get More Offer</div>
<h2 class="abs center display news-title">Subscribe Newsletters<br>To Get More Updates</h2>
<div class="abs news-input">Email address</div>
<a class="abs btn news-btn">Subscribe</a>

<!-- footer -->
<div class="abs brand foot-brand"><span class="brand-dot" style="width:18px;height:18px"></span>Brightmara Sun</div>
<h4 class="abs foot-head" style="left:434px">QUICK LINKS</h4>
<div class="abs foot-links">Latest Services<br>Meet Team Member<br>Latest News &amp; Blog<br>Company History<br>Global Services<br>Contact With Us</div>
<h4 class="abs foot-head" style="left:620px">LATEST NEWS</h4>
<div class="abs news-item" style="top:3528px"><div class="news-thumb" role="img" aria-label="Solar farm news photo"></div><div><h5>Powering Asia Pacific's Energy Transition</h5><small>December 09</small></div></div>
<div class="abs news-item" style="top:3604px"><div class="news-thumb" role="img" aria-label="Solar panel news photo"></div><div><h5>Powering Asia Pacific's Energy Transition</h5><small>December 09</small></div></div>
<h4 class="abs foot-head" style="left:907px">CONTACT US</h4>
<div class="abs contact-list">
  <div><svg width="10" height="13" viewBox="0 0 10 13"><path d="M5 0a5 5 0 0 1 5 5c0 4-5 8-5 8S0 9 0 5a5 5 0 0 1 5-5z" fill="#c50d0d"/><circle cx="5" cy="5" r="2" fill="#fff"/></svg><span>48 Harbor Lane, Sun Court,<br>Albany</span></div>
  <div><svg width="11" height="9" viewBox="0 0 26 20"><rect width="26" height="20" rx="2" fill="#c50d0d"/><path d="M1 2l12 9 12-9" fill="none" stroke="#fff" stroke-width="2"/></svg><span>hello@brightmarasun.com</span></div>
  <div><svg width="11" height="11" viewBox="0 0 24 24"><path d="M6.6 10.8a15 15 0 0 0 6.6 6.6l2.2-2.2c.3-.3.7-.4 1-.2 1.1.4 2.3.6 3.6.6.6 0 1 .4 1 1V20c0 .6-.4 1-1 1A17 17 0 0 1 3 4c0-.6.4-1 1-1h3.5c.6 0 1 .4 1 1 0 1.2.2 2.4.6 3.6.1.3 0 .7-.2 1z" fill="#c50d0d"/></svg><span>+012 (555) 0192</span></div>
</div>
<div class="abs socials"><i style="background:#3b5998"></i><i style="background:#1da1f2"></i><i style="background:#db4437"></i><i style="background:#0e76a8"></i></div>

<div class="abs copybar">Copyright 2021 | All Rights reserved</div>
<div class="abs to-top"><svg width="12" height="8" viewBox="0 0 12 8" aria-hidden="true"><path d="M1 7l5-5 5 5" fill="none" stroke="#fff" stroke-width="1.8"/></svg></div>

</body>
</html>
```